Veldantic Mailer

We are a side sewer repair and replacement contractor in the Seattle Washington market called Veldantic Technologies. We offer our services on a business to business basis to plumbing contractors. The concept is that plumbers get calls from their customer to excavate and repair underground drainage pipes but most plumbers don't like to dig. So we offer to maximize their marketing dollars by helping them with a service that they are either not prepared to offer their customers or just plain don't want to offer. We pride ourselves on our great capacity (lots of equipment and lots of well trained technicians) and our ability to respond quickly to the needs of our customers clients.So I would like to see a design that shows something like an army of mini-excavators, some bigger than others as well as a large crew of construction workers. The workers should look fit (but not huge and bulky), intelligent, wearing safety equipment and even maybe a little bit futuristic. It will be a two sided mailer. So one side could feature our logo and pictures of key members of our organization and what they do and the other could feature our army of equipment and field personnel along with the key components of our service offering. The TWRA logo would need to be included as well.
Target Market(s)
Plumbing contractors
Industry/Entity Type
Construction
Colors
Designer to choose colors to be used in the design.
Look and feel

```html
<!DOCTYPE html>
<html lang="en">
<head>
<meta charset="utf-8">
<title>Veldantic Mailer</title>
<link href="https://fonts.googleapis.com/css2?family=Open+Sans:wght@400;600&family=Roboto:wght@400;500;700&display=swap" rel="stylesheet">
<style>
  :root {
    --page: #e6e4e0;
    --card: #ffffff;
    --red: #d3113f;
    --ink: #2b2b2b;
    --muted: #555555;
    --panel: #f1f1f1;
    --bar: #dadada;
    --photo-a: #8fa6bd;
    --photo-b: #2f3d57;
    --line: #9a9a9a;
  }
  * { box-sizing: border-box; margin: 0; padding: 0; }
  html, body { width: 1200px; height: 900px; overflow: hidden; }
  body {
    background: var(--page);
    font-family: "Roboto", Arial, sans-serif;
    color: var(--ink);
    position: relative;
  }
  .card {
    position: absolute;
    width: 570px;
    height: 390px;
    background: var(--card);
    box-shadow: 0 6px 18px rgba(0,0,0,.18);
    overflow: hidden;
  }
  .card--front { left: 24px; top: 140px; }
  .card--back { left: 606px; top: 370px; }

  /* front side */
  .hero-photo {
    position: absolute; left: 0; top: 0; width: 292px; height: 390px;
    background: linear-gradient(160deg, #c9d3dc 0%, var(--photo-a) 35%, var(--photo-b) 100%);
  }
  .accent-rule {
    position: absolute; top: 0; bottom: 0; width: 5px; background: var(--red);
  }
  .card--front .accent-rule { left: 292px; top: 58px; }
  .dark-strip {
    position: absolute; left: 280px; top: 0; width: 12px; height: 58px;
    background: linear-gradient(#49556a, #2f3d57);
  }
  .front-panel {
    position: absolute; left: 297px; top: 0; right: 0; bottom: 0;
    padding: 18px 16px 0 52px; text-align: right;
  }
  .brand {
    font-family: "Open Sans", Arial, sans-serif;
    font-weight: 400; color: var(--ink); line-height: 1.05;
  }
  .brand__name { font-size: 30px; display: block; }
  .brand__sub { font-size: 13px; display: block; }
  .tagline { font-size: 8px; letter-spacing: .5px; margin-top: 14px; color: var(--muted); }
  .headline { font-size: 17px; font-weight: 700; color: var(--red); letter-spacing: .3px; }
  .subhead { font-size: 10px; font-weight: 700; color: var(--red); margin-top: 12px; }
  .body-copy { font-size: 8px; line-height: 1.4; color: var(--muted); margin-top: 4px; }
  .goal { font-size: 9.5px; line-height: 1.35; color: var(--ink); margin-top: 8px; }
  .goal-list { list-style: none; font-size: 8px; line-height: 1.45; color: var(--muted); margin-top: 6px; }
  .goal-list li { margin-bottom: 4px; }
  .portrait {
    position: absolute; width: 46px; height: 46px; border-radius: 50%;
    border: 3px solid #fff; box-shadow: 0 0 0 1.5px var(--red);
    background: radial-gradient(circle at 40% 35%, #9fb4c8, #3c4d66);
  }
  .card--front .portrait--one { left: 272px; top: 150px; }
  .card--front .portrait--two { left: 272px; top: 202px; }
  .contact-bar {
    position: absolute; bottom: 0; height: 28px;
    background: var(--bar); display: flex; align-items: center;
    gap: 28px; padding-left: 16px; font-size: 7.5px; color: var(--muted);
  }
  .card--front .contact-bar { left: 297px; right: 0; }
  .contact-item { display: flex; align-items: center; gap: 5px; }
  .contact-item svg { width: 9px; height: 9px; fill: var(--ink); }

  /* back side */
  .offer-panel {
    position: absolute; left: 0; top: 0; width: 330px; height: 362px;
    background: linear-gradient(#ffffff 0%, #ffffff 18%, var(--panel) 18%);
    padding: 78px 22px 0 18px;
  }
  .offer-panel .subhead { margin-top: 0; font-size: 11px; }
  .offer-intro { font-size: 7.5px; line-height: 1.4; color: var(--muted); margin-top: 4px; }
  .offer-list { list-style: none; font-size: 7.5px; line-height: 1.42; color: var(--ink); margin-top: 6px; }
  .offer-list li { padding-left: 10px; position: relative; }
  .offer-list li::before {
    content: ""; position: absolute; left: 0; top: 4px;
    width: 4px; height: 4px; background: var(--red);
  }
  .feature-copy { font-size: 7.5px; line-height: 1.4; color: var(--muted); margin-top: 3px; }
  .offer-panel .feature-title { margin-top: 9px; }
  .card--back .accent-rule { left: 330px; top: 64px; }
  .card--back .portrait--one { left: 309px; top: 128px; }
  .card--back .portrait--two { left: 309px; top: 182px; }
  .card--back .contact-bar { left: 0; width: 330px; }
  .address-side {
    position: absolute; left: 335px; top: 0; right: 0; bottom: 0;
  }
  .address-side .brand { position: absolute; left: 48px; top: 58px; }
  .address-side .brand__name { font-size: 22px; }
  .address-side .brand__sub { font-size: 10px; }
  .stamp-box {
    position: absolute; right: 22px; top: 20px; width: 50px; height: 56px;
    border: 1.5px solid #b5b5b5;
  }
  .address-lines { position: absolute; left: 62px; right: 22px; top: 150px; }
  .address-lines span { display: block; height: 26px; border-bottom: 1px solid var(--line); }
</style>
</head>
<body>

<section class="card card--front" aria-label="Mailer front">
  <div class="hero-photo" role="img" aria-label="Photo of a smiling technician in hard hat and work overalls carrying cable in an industrial plant"></div>
  <div class="dark-strip"></div>
  <div class="accent-rule"></div>
  <div class="portrait portrait--one" role="img" aria-label="Photo of a plumber at work"></div>
  <div class="portrait portrait--two" role="img" aria-label="Photo of a technician inspecting pipes"></div>
  <div class="front-panel">
    <p class="brand"><span class="brand__name">Veldantic</span><span class="brand__sub">Technologies LLC</span></p>
    <p class="tagline">WE PROVIDE BEST</p>
    <h1 class="headline">PLUMBING SERVICE</h1>
    <h2 class="subhead">WHAT DO WE DO?</h2>
    <p class="body-copy">Veldantic Technologies is in business to enhance the service offering of the area plumber.</p>
    <p class="goal">At Veldantic Technologies it is our goal to:</p>
    <ul class="goal-list">
      <li>Increase your profitability</li>
      <li>Provide the latest work environment &amp; the right crew</li>
      <li>Maximize your marketing dollars &amp; help you retain your customers</li>
    </ul>
  </div>
  <div class="contact-bar">
    <span class="contact-item"><svg viewBox="0 0 24 24"><path d="M6.6 10.8a15.1 15.1 0 0 0 6.6 6.6l2.2-2.2a1 1 0 0 1 1-.25 11.4 11.4 0 0 0 3.6.57 1 1 0 0 1 1 1V20a1 1 0 0 1-1 1A17 17 0 0 1 3 4a1 1 0 0 1 1-1h3.5a1 1 0 0 1 1 1c0 1.25.2 2.45.57 3.57a1 1 0 0 1-.25 1z"/></svg>XXXXXXXXX</span>
    <span class="contact-item"><svg viewBox="0 0 24 24"><circle cx="12" cy="12" r="10"/></svg>Your Website Goes Here</span>
  </div>
</section>

<section class="card card--back" aria-label="Mailer back">
  <div class="offer-panel">
    <h2 class="subhead">OUR SERVICE OFFERING</h2>
    <p class="offer-intro">By utilizing our personnel and equipment you will see a significant increase in profitability. By partnering with us you can sell our equipment and personnel as if they are your equipment and personnel.</p>
    <ul class="offer-list">
      <li>8 Professionally Trained Excavation Crews</li>
      <li>2 Cast In Place Pipe Installation Set-Ups</li>
      <li>Pipe Bursting Equipment</li>
      <li>Sewer Camera and Locating Service</li>
      <li>3 Hydro Jetters</li>
      <li>Concrete Cutting and Replacement</li>
      <li>Water Line Repair and Replacement</li>
      <li>Concrete and Asphalt Repair and Replacement</li>
      <li>Repairs in the City Right-of-Way</li>
      <li>Residential/Commercial</li>
      <li>Drain Cleaning and Maintenance</li>
      <li>Certified Technicians</li>
      <li>24/7/365 Emergency Service</li>
    </ul>
    <h2 class="subhead feature-title">FEATURE</h2>
    <p class="feature-copy">Safety First! All of our personnel is trained to perform each job with safety in mind. Our development of best sales practices has resulted in repeat business with maximum customer satisfaction.</p>
  </div>
  <div class="accent-rule"></div>
  <div class="portrait portrait--one" role="img" aria-label="Photo of a field technician"></div>
  <div class="portrait portrait--two" role="img" aria-label="Photo of a team member at a work van"></div>
  <div class="contact-bar">
    <span class="contact-item"><svg viewBox="0 0 24 24"><path d="M6.6 10.8a15.1 15.1 0 0 0 6.6 6.6l2.2-2.2a1 1 0 0 1 1-.25 11.4 11.4 0 0 0 3.6.57 1 1 0 0 1 1 1V20a1 1 0 0 1-1 1A17 17 0 0 1 3 4a1 1 0 0 1 1-1h3.5a1 1 0 0 1 1 1c0 1.25.2 2.45.57 3.57a1 1 0 0 1-.25 1z"/></svg>XXXXXXXXX</span>
    <span class="contact-item"><svg viewBox="0 0 24 24"><circle cx="12" cy="12" r="10"/></svg>Your Website Goes Here</span>
  </div>
  <div class="address-side">
    <p class="brand"><span class="brand__name">Veldantic</span><span class="brand__sub">Technologies LLC</span></p>
    <div class="stamp-box"></div>
    <div class="address-lines"><span></span><span></span><span></span><span></span></div>
  </div>
</section>

</body>
</html>
```